New Corporate Email footer (business card design) for 40th Anniversary for Timber Traders

We are traders in sustainable timber worldwide, specialising in tropical hardwoods.
We need to keep our current company logo, but update our email footer with a business card like design which marks the company's 40th Anniversary. 1981-2021. We would need:
Company Logo, Name and Address, website
Sender's: Name, Tel no, fax no, email address
We would need this in a format which we could update ourselves re names/phone numbers if any change.

Target Market(s)

Customers, suppliers, service providers

Contact Information for Business Card

Maria Denton
Tel: +44 (0) 208 734 2216
Fax: +44 (0) 208 734 5580
Email: maria@pvrwoodline.co.uk
Web: www.pvrwoodline.co.uk

PVR Woodline Ltd. 17 Bramble Court, Ashford Lane, Hollowmere, Surrey KT5 3QW, UNITED KINGDOM

IMPORTANT NOTICE - This message contains confidential information for the intended addressee only. Any views expressed are those of the sender not PVR Woodline Ltd unless otherwise stated. If you receive this message [and any attachment(s)] in error you must not store, copy, disclose or otherwise use any part of it and should advise the sender immediately on 020 8734 9162. Internet communications are not guaranteed secure or virus free. PVR reserves the right to monitor all e-mail communications and does not accept responsibility for any loss or damage resulting from access of this e-mail or any file(s) attached.

Font styles to use
Sans Serif
Other font styles liked:
• not actually sure

Requirements
Must have
• mention of company's 40th Anniversary 1981-2021, which is the whole point of the design
Nice to have
• Our company colour is British Racing Green, but any green theme may be good
Maybe a tree design but allowing the company logo to stand out.

```html
<!DOCTYPE html>
<html lang="en">
<head>
<meta charset="utf-8">
<title>PVR Woodline – Email Footer</title>
<link rel="stylesheet" href="https://fonts.googleapis.com/css2?family=Lato:wght@400;700&display=swap">
<style>
  :root {
    --backdrop: #dcdcdc;
    --card: #ffffff;
    --ink: #1f2a22;
    --racing-green: #1e3b26;
    --notice-green: #3f5f35;
    --rule: #1f2a22;
    --gold-light: #f7d46a;
    --gold-dark: #c98a12;
  }
  * { margin: 0; padding: 0; box-sizing: border-box; }
  html, body {
    width: 1200px; height: 756px; overflow: hidden;
    background: var(--backdrop);
    font-family: "Lato", Arial, sans-serif;
    color: var(--ink);
  }
  .footer-card {
    position: absolute; left: 142px; top: 223px;
    width: 938px; height: 321px;
    background: var(--card);
    box-shadow: 2px 4px 6px rgba(0,0,0,0.45);
  }
  .sender-name {
    position: absolute; left: 63px; top: 32px;
    font-size: 25px; font-weight: 700; color: var(--racing-green);
  }
  .contact-list { position: absolute; left: 62px; top: 80px; list-style: none; }
  .contact-list li {
    display: flex; align-items: center; height: 26px;
    font-size: 21px; color: var(--ink);
  }
  .contact-list svg { width: 19px; height: 19px; margin-right: 9px; fill: var(--ink); }
  .brand-mark {
    position: absolute; left: 352px; top: 52px; width: 132px;
    display: flex; flex-direction: column; align-items: center;
  }
  .brand-mark .brand-dot {
    width: 64px; height: 64px; border-radius: 50%; background: var(--racing-green);
  }
  .brand-mark .brand-name {
    margin-top: 10px; text-align: center; white-space: nowrap;
    font-size: 19px; font-weight: 400; color: var(--ink);
  }
  .company-address {
    position: absolute; left: 507px; top: 27px;
    font-size: 21px; line-height: 26px; color: var(--ink); font-style: normal;
  }
  .anniversary-badge {
    position: absolute; left: 760px; top: 28px; width: 129px; height: 102px;
    border-radius: 50% 50% 40% 40%;
    background: radial-gradient(circle at 50% 40%, var(--gold-light), var(--gold-dark));
  }
  .anniversary-years {
    position: absolute; left: 760px; top: 140px; width: 129px;
    text-align: center; font-size: 19px; color: var(--ink);
  }
  .divider {
    position: absolute; left: 59px; top: 204px; width: 712px; height: 4px;
    background: var(--rule);
  }
  .social-links { position: absolute; left: 780px; top: 193px; display: flex; gap: 5px; }
  .social-links span {
    width: 23px; height: 23px; border-radius: 50%; background: var(--racing-green);
  }
  .legal-notice {
    position: absolute; left: 40px; top: 225px; width: 858px;
    text-align: center; font-size: 13.6px; line-height: 16.3px; color: var(--notice-green);
  }
</style>
</head>
<body>
  <section class="footer-card">
    <h1 class="sender-name">Maria Denton</h1>
    <ul class="contact-list">
      <li><svg viewBox="0 0 24 24" aria-hidden="true"><path d="M6.6 10.8a15 15 0 0 0 6.6 6.6l2.2-2.2c.3-.3.7-.4 1-.2 1.1.4 2.3.6 3.6.6.6 0 1 .4 1 1V20c0 .6-.4 1-1 1A17 17 0 0 1 3 4c0-.6.4-1 1-1h3.5c.6 0 1 .4 1 1 0 1.3.2 2.5.6 3.6.1.3 0 .7-.2 1z"/></svg>+44 (0) 208 734 2216</li>
      <li><svg viewBox="0 0 24 24" aria-hidden="true"><path d="M6 2h12v5H6zM4 8h16a2 2 0 0 1 2 2v6h-4v5H6v-5H2v-6a2 2 0 0 1 2-2zm4 8v3h8v-3z"/></svg>+44 (0) 208 734 5580</li>
      <li><svg viewBox="0 0 24 24" aria-hidden="true"><path d="M2 5h20v14H2zm2 2v.5l8 5 8-5V7z"/></svg>maria@pvrwoodline.co.uk</li>
      <li><svg viewBox="0 0 24 24" aria-hidden="true"><path d="M12 2a10 10 0 1 0 0 20 10 10 0 0 0 0-20zm0 2c.9 1.2 1.6 2.7 2 4h-4c.4-1.3 1.1-2.8 2-4zM4.3 14a8 8 0 0 1 0-4h3.4a16 16 0 0 0 0 4zm.9 2h3a15 15 0 0 0 1.4 3.6A8 8 0 0 1 5.2 16zm3-8h-3a8 8 0 0 1 4.4-3.6A15 15 0 0 0 8.2 8zM12 20c-.9-1.2-1.6-2.7-2-4h4c-.4 1.3-1.1 2.8-2 4zm2.3-6H9.7a14 14 0 0 1 0-4h4.6a14 14 0 0 1 0 4zm.1 5.6a15 15 0 0 0 1.4-3.6h3a8 8 0 0 1-4.4 3.6zm1.9-5.6a16 16 0 0 0 0-4h3.4a8 8 0 0 1 0 4zm-.5-6a15 15 0 0 0-1.4-3.6A8 8 0 0 1 18.8 8z"/></svg>www.pvrwoodline.co.uk</li>
    </ul>

    <div class="brand-mark">
      <span class="brand-dot" aria-hidden="true"></span>
      <span class="brand-name">PVR Woodline</span>
    </div>

    <address class="company-address">
      PVR Woodline Ltd.<br>
      17 Bramble Court,<br>
      Ashford Lane,<br>
      Hollowmere, Surrey<br>
      KT5 3QW,<br>
      UNITED KINGDOM
    </address>

    <div class="anniversary-badge" role="img" aria-label="Gold laurel wreath badge with ribbon marking the 40th anniversary"></div>
    <p class="anniversary-years">1981-2021</p>

    <div class="divider"></div>
    <div class="social-links">
      <span role="img" aria-label="Social network link"></span>
      <span role="img" aria-label="Video channel link"></span>
      <span role="img" aria-label="Microblog link"></span>
    </div>

    <p class="legal-notice">
      IMPORTANT NOTICE - This message contains confidential information for the intended addressee only. Any views expressed<br>
      are those of the sender not PVR Woodline Ltd unless otherwise stated. If you receive this message [and any attachment(s)] in error<br>
      you must not store, copy, disclose or otherwise use any part of it and should advise the sender immediately on 020 8734 9162.<br>
      Internet communications are not guaranteed secure or virus free. PVR reserves the right to monitor all e-mail communications<br>
      and does not accept responsibility for any loss or damage resulting from access of this e-mail or any file(s) attached.
    </p>
  </section>
</body>
</html>
```